Business Card

I need a business card for a nutrition/fitness consultant. We are a personalized and online service that caters to developing individual plans based on persons needs. I will send you information to need on card as well as logo. Last business card was grey background and writing was black and red. I think a pic on the backside (maybe a photo that is on the app) would be good?

HelloMarlo (Ill send you logo)
Marlo Venti, Registered Nurse and Certified Sports Nutrionist (R.N., C.S.N.)
Personalized Nutrition and Fitness Architecture

1-800-555-0147 office
(305) 555-0182 cell
website www.hellomarlo-demo.com
marlo@hellomarlo-demo.com

Two locations so maybe two cards
2180 Willowbend Lane, inside Sunpeak Glow Studio
Coral Gables, Fl 33199

and
7300 W Orchard Parkway
Boca Raton, Florida 33498

Requirements
Must have
• I guess the logo we provide so it is consistent with the new website etc

```html
<!DOCTYPE html>
<html lang="en">
<head>
<meta charset="utf-8">
<title>HelloMarlo Business Card</title>
<link rel="stylesheet" href="https://fonts.googleapis.com/css2?family=Arimo:wght@400;700&display=swap">
<style>
  :root {
    --stage: #666666;
    --card: #f0f0f2;
    --ink: #111111;
    --brand-red: #9a0a0e;
    --photo-light: #f4f4f4;
    --photo-mid: #c9c9c9;
    --photo-dark: #8a8a8a;
    --white: #ffffff;
  }
  * { margin: 0; padding: 0; box-sizing: border-box; }
  html, body {
    width: 1200px;
    height: 900px;
    overflow: hidden;
    background: var(--stage);
    font-family: "Arimo", Arial, sans-serif;
    color: var(--ink);
  }
  .canvas { position: relative; width: 1200px; height: 900px; }

  .card {
    position: absolute;
    border-radius: 24px;
    overflow: hidden;
    box-shadow: 0 2px 6px rgba(0,0,0,0.25);
  }

  /* Front card */
  .card--front {
    left: 254px; top: 46px; width: 689px; height: 400px;
    background: var(--white);
  }
  .portrait {
    position: absolute; inset: 0;
    background:
      radial-gradient(ellipse 260px 320px at 52% 40%, var(--photo-mid) 0%, #dcdcdc 55%, transparent 80%),
      linear-gradient(90deg, #e6e6e6 0%, var(--photo-light) 30%, #fafafa 75%, var(--white) 100%);
  }
  .brand-mark {
    position: absolute;
    display: flex; align-items: center; gap: 8px;
    font-weight: 700;
    color: var(--ink);
    letter-spacing: -0.5px;
  }
  .brand-mark__dot {
    width: 14px; height: 14px; border-radius: 50%;
    background: var(--brand-red);
  }
  .card--front .brand-mark { right: 14px; top: 40px; font-size: 26px; }
  .web-band {
    position: absolute; left: 0; right: 0; top: 287px; height: 85px;
    background: var(--brand-red);
    display: flex; align-items: center; justify-content: center;
    color: var(--white);
    font-size: 22px;
  }

  /* Back card */
  .card--back {
    left: 249px; top: 455px; width: 691px; height: 402px;
    background: var(--card);
  }
  .card--back .brand-mark { left: 38px; top: 62px; font-size: 26px; }
  .identity {
    position: absolute; right: 52px; top: 72px;
    text-align: right;
  }
  .identity__name {
    font-size: 27px; font-weight: 700;
    margin-right: 8px;
    line-height: 1.2;
  }
  .identity__title {
    margin-top: 16px;
    font-size: 14.5px;
    line-height: 1.2;
  }
  .contact {
    position: absolute; right: 52px; top: 210px;
    list-style: none;
    text-align: right;
    font-size: 14.5px;
    line-height: 19.7px;
  }
  .contact__indent { padding-right: 4px; }
  .contact strong { font-weight: 700; }
</style>
</head>
<body>
<main class="canvas">

  <section class="card card--front">
    <div class="portrait" role="img" aria-label="Black and white portrait photograph of the consultant with long light hair"></div>
    <div class="brand-mark"><span class="brand-mark__dot"></span>HelloMarlo</div>
    <div class="web-band">www.hellomarlo-demo.com</div>
  </section>

  <section class="card card--back">
    <div class="brand-mark"><span class="brand-mark__dot"></span>HelloMarlo</div>
    <div class="identity">
      <h1 class="identity__name">Marlo Venti</h1>
      <p class="identity__title">Registered Nurse and Certified Sports Nutrionist (R.N., C.S.N.)</p>
    </div>
    <ul class="contact">
      <li class="contact__indent">1-800-555-0147</li>
      <li class="contact__indent">(305) 555-0182</li>
      <li>www.hellomarlo-demo.com</li>
      <li>marlo@hellomarlo-demo.com</li>
      <li><strong>2180 W</strong>illowbend Lane</li>
      <li>inside Sunpeak Glow Studio</li>
      <li>Coral Gables, Fl 33199</li>
    </ul>
  </section>

</main>
</body>
</html>
```